Brisk Nest - Business Card

Modern Business Card : I like a simple, clean designs. Think Quill!

Information to Include
Brisk Nest Inc. (Logo)
Name: Ted Marsh
Position: President
Office: 987-654-3210
Fax: 987-654-3210
Cell: 987-654-3210
E-Mail: tmarsh@thebrisknest.example
Website: www.thebrisknest.example

I attached the "gatebell.example" dealer logo. This logo is not a requirement, but a plus if it looks good with the design.

I also have access to more pictures and logos, if you see something on gatebell.example
or 7orb.example, I can probably get the file. Again, this is not mandatory.

```html
<!DOCTYPE html>
<html lang="en">
<head>
<meta charset="utf-8">
<title>Brisk Nest – Business Card</title>
<link rel="stylesheet" href="https://fonts.googleapis.com/css2?family=Exo+2:wght@400;500;700&display=swap">
<style>
  :root {
    --page: #ece9e4;
    --orange: #cf5a2c;
    --black: #0c0c0c;
    --white: #ffffff;
    --panel-shade: #ececec;
    --ink: #2b2b2b;
    --contact-ink: #3a1e12;
    --accent: #29b6d6;
  }
  * { box-sizing: border-box; margin: 0; padding: 0; }
  html, body { width: 1200px; height: 1019px; overflow: hidden; }
  body {
    background: var(--page);
    font-family: "Exo 2", sans-serif;
    position: relative;
  }
  .card {
    position: absolute;
    left: 320px;
    width: 560px;
    height: 320px;
    background: var(--orange);
    box-shadow: 0 10px 30px rgba(0,0,0,0.18);
    overflow: hidden;
  }
  .card--front { top: 150px; }
  .card--back { top: 549px; }

  /* Front */
  .identity-panel {
    position: absolute;
    left: 36px; top: 36px;
    width: 264px; height: 248px;
    background: radial-gradient(circle at 50% 40%, var(--white) 40%, var(--panel-shade) 100%);
  }
  .brand {
    position: absolute;
    left: 30px; top: 58px;
    display: flex; align-items: center; gap: 10px;
  }
  .brand__square { width: 22px; height: 22px; background: var(--orange); }
  .brand__name {
    font-weight: 700; font-size: 28px; color: var(--ink); letter-spacing: 0.2px;
    white-space: nowrap;
  }
  .person { position: absolute; left: 30px; bottom: 44px; }
  .person__name {
    font-weight: 700; font-size: 27px; color: var(--ink);
    text-transform: uppercase; letter-spacing: 0.5px; line-height: 1;
  }
  .person__role { font-size: 17px; color: var(--ink); margin-top: 4px; }

  .contact-frame {
    position: absolute;
    left: 300px; top: 0;
    width: 260px; height: 320px;
    background: var(--black);
  }
  .contact-panel {
    position: absolute;
    left: 0; top: 36px;
    width: 224px; height: 248px;
    background: var(--orange);
    padding: 44px 0 0 18px;
  }
  .contact-list { list-style: none; }
  .contact-list li {
    display: flex; align-items: center; gap: 8px;
    font-size: 11.5px; color: var(--contact-ink);
    line-height: 1.3; margin-bottom: 13px;
    white-space: nowrap;
  }
  .contact-list svg { flex: 0 0 11px; width: 11px; height: 11px; fill: var(--accent); }
  .contact-list__label { font-weight: 500; }

  /* Back */
  .back-frame {
    position: absolute; inset: 0;
    border: 40px solid var(--black);
  }
  .back-panel {
    position: absolute;
    left: 40px; top: 40px; right: 40px; bottom: 40px;
    background: var(--orange);
  }
  .back-inset {
    position: absolute;
    left: 70px; top: 70px;
    width: 160px; height: 90px;
    background: var(--white);
  }
</style>
</head>
<body>
  <section class="card card--front" aria-label="Business card front">
    <div class="identity-panel">
      <div class="brand">
        <span class="brand__square"></span>
        <span class="brand__name">Brisk Nest</span>
      </div>
      <div class="person">
        <p class="person__name">Ted Marsh</p>
        <p class="person__role">President</p>
      </div>
    </div>
    <div class="contact-frame">
      <div class="contact-panel">
        <ul class="contact-list">
          <li>
            <svg viewBox="0 0 12 12"><path d="M2.5 0.5l2 2.5-1.2 1.4a7 7 0 0 0 4.3 4.3L9 7.5l2.5 2-1.5 2C5 11.5 0.5 7 0.5 2z"/></svg>
            <span><span class="contact-list__label">Office:</span> 987-654-3210</span>
          </li>
          <li>
            <svg viewBox="0 0 12 12"><path d="M3 0h6v3H3zM0 4h12v6H9v2H3v-2H0zM4 8v3h4V8z"/></svg>
            <span><span class="contact-list__label">Fax:</span> 987-654-3210</span>
          </li>
          <li>
            <svg viewBox="0 0 12 12"><path d="M3 0h6v12H3zM4 1v9h4V1z"/></svg>
            <span><span class="contact-list__label">Cell:</span> 987-654-3210</span>
          </li>
          <li>
            <svg viewBox="0 0 12 12"><path d="M0 2h12v8H0zM1 3l5 3.5L11 3v-.2H1z"/></svg>
            <span>tmarsh@thebrisknest.example</span>
          </li>
          <li>
            <svg viewBox="0 0 12 12"><circle cx="6" cy="6" r="6"/></svg>
            <span>www.thebrisknest.example</span>
          </li>
        </ul>
      </div>
    </div>
  </section>

  <section class="card card--back" aria-label="Business card back">
    <div class="back-panel"></div>
    <div class="back-frame"></div>
    <div class="back-inset"></div>
  </section>
</body>
</html>
```